Pharmacy ad

need 2 pharmacy ads for the phone book. one for Brook Pharmacy and one for Oakvale Care Pharmacy. Dimensions for ad is 4.75in x 4.667 in. please see attached examples of ad uploaded as well logos of each pharmacy

```html
<!DOCTYPE html>
<html lang="en">
<head>
<meta charset="utf-8">
<title>Oakvale Care Pharmacy – Directory Ad</title>
<link href="https://fonts.googleapis.com/css2?family=Montserrat:wght@400;600;800&family=Source+Sans+3:ital,wght@1,400;1,700&display=swap" rel="stylesheet">
<style>
  :root {
    --green: #7dc142;
    --blue: #4a5da9;
    --yellow: #fecb00;
    --pill: #fbbd2a;
    --orange: #f26522;
    --white: #ffffff;
  }
  html, body { margin: 0; padding: 0; overflow: hidden; }
  .ad {
    position: relative;
    width: 1200px;
    height: 1180px;
    overflow: hidden;
    background: var(--yellow);
    font-family: "Source Sans 3", sans-serif;
    color: var(--blue);
  }
  .masthead {
    position: absolute; left: 0; top: 0; width: 1200px; height: 219px;
    background: var(--white);
  }
  .headline {
    position: absolute; left: 66px; top: 52px; margin: 0;
    font-family: "Montserrat", sans-serif; font-weight: 800;
    font-size: 63px; line-height: 52px; color: var(--green);
    letter-spacing: 1px;
  }
  .brand {
    position: absolute; left: 672px; top: 78px;
    display: flex; align-items: center; gap: 18px;
  }
  .brand-dot { width: 54px; height: 54px; border-radius: 50%; background: var(--blue); }
  .brand-name {
    font-family: "Montserrat", sans-serif; font-weight: 600;
    font-size: 38px; line-height: 44px; color: var(--blue);
  }
  .discount-band {
    position: absolute; left: 0; top: 219px; width: 1200px; height: 101px;
    background: var(--blue);
  }
  .band-rule {
    position: absolute; left: 0; top: 320px; width: 1200px; height: 12px;
    background: var(--green);
  }
  .band-label {
    position: absolute; color: var(--white);
    font-style: italic; font-weight: 700; font-size: 35px; line-height: 30px;
  }
  .senior { left: 67px; top: 254px; }
  .student { left: 835px; top: 240px; }
  .student span { display: block; font-weight: 400; }
  .rate {
    position: absolute; left: 476px; top: 196px;
    font-family: "Montserrat", sans-serif; font-weight: 600;
    font-size: 142px; line-height: 142px; color: var(--white); letter-spacing: -4px;
  }
  .rate-caption {
    position: absolute; left: 503px; top: 318px;
    font-style: italic; font-weight: 700; font-size: 38px; line-height: 38px;
    color: var(--orange);
  }
  .services { position: absolute; left: 0; top: 383px; margin: 0; padding: 0; list-style: none; }
  .services li {
    position: relative; height: 52px;
    font-style: italic; font-weight: 700; font-size: 39px; line-height: 44px;
    padding-left: 93px;
  }
  .services li::after {
    content: ""; position: absolute; left: 80px; top: 48px;
    width: var(--rule, 360px); height: 2px; background: var(--green); opacity: .8;
  }
  .services li:last-child::after { display: none; }
  .services svg { position: absolute; left: 29px; top: 16px; }
  .delivery-pill {
    position: absolute; left: 791px; top: 402px; width: 440px; height: 52px;
    border-radius: 26px 0 0 26px; background: var(--pill);
    color: var(--white); font-style: italic; font-weight: 700;
    font-size: 37px; line-height: 52px; padding-left: 42px; box-sizing: border-box;
  }
  .hours { position: absolute; left: 835px; top: 469px; font-style: italic; font-size: 35px; line-height: 42px; }
  .hours .day { font-weight: 700; }
  .hours .time { font-weight: 400; }
  .product-display {
    position: absolute; left: 34px; top: 749px; width: 1131px; height: 345px;
    border-radius: 16px;
    background: linear-gradient(100deg, rgba(255,255,255,.55), rgba(120,210,220,.35) 45%, rgba(255,255,255,.5));
  }
  .contact-pin { position: absolute; left: 21px; top: 1107px; }
  .address {
    position: absolute; left: 73px; top: 1108px;
    font-family: "Montserrat", sans-serif; font-weight: 400;
    font-size: 18.5px; line-height: 22px;
  }
  .phone-icon { position: absolute; left: 368px; top: 1100px; }
  .phone-number {
    position: absolute; left: 434px; top: 1082px;
    font-family: "Montserrat", sans-serif; font-weight: 600;
    font-size: 86px; line-height: 90px; letter-spacing: 1px;
  }
  .social { position: absolute; left: 997px; top: 1118px; display: flex; align-items: center; gap: 10px;
    font-style: italic; font-size: 26px; }
  .social-square { width: 31px; height: 31px; background: var(--blue); border-radius: 4px; }
</style>
</head>
<body>
<div class="ad">
  <header class="masthead">
    <h1 class="headline">WHERE GOOD<br>HEALTH BEGINS</h1>
    <div class="brand">
      <div class="brand-dot"></div>
      <div class="brand-name">Oakvale Care<br>Pharmacy</div>
    </div>
  </header>

  <div class="discount-band"></div>
  <div class="band-rule"></div>
  <div class="band-label senior">Senior Citizen discount</div>
  <div class="rate">10%</div>
  <div class="rate-caption">DISCOUNT ON</div>
  <div class="band-label student">Student discount<span>with valid ID card</span></div>

  <ul class="services">
    <li style="--rule:360px"><svg width="34" height="22" viewBox="0 0 34 22"><path d="M2 12 L12 19 L32 3" fill="none" stroke="#f26522" stroke-width="4" stroke-linecap="round" stroke-linejoin="round"/></svg>Certified Pharmacists</li>
    <li style="--rule:450px"><svg width="34" height="22" viewBox="0 0 34 22"><path d="M2 12 L12 19 L32 3" fill="none" stroke="#f26522" stroke-width="4" stroke-linecap="round" stroke-linejoin="round"/></svg>Affordable prices</li>
    <li style="--rule:510px"><svg width="34" height="22" viewBox="0 0 34 22"><path d="M2 12 L12 19 L32 3" fill="none" stroke="#f26522" stroke-width="4" stroke-linecap="round" stroke-linejoin="round"/></svg>Brand &amp; Generic Medicines</li>
    <li style="--rule:550px"><svg width="34" height="22" viewBox="0 0 34 22"><path d="M2 12 L12 19 L32 3" fill="none" stroke="#f26522" stroke-width="4" stroke-linecap="round" stroke-linejoin="round"/></svg>Blood Pressure &amp;&nbsp; Glucose checks</li>
    <li style="--rule:520px"><svg width="34" height="22" viewBox="0 0 34 22"><path d="M2 12 L12 19 L32 3" fill="none" stroke="#f26522" stroke-width="4" stroke-linecap="round" stroke-linejoin="round"/></svg>Personal care &amp; Beauty Products</li>
    <li style="--rule:252px"><svg width="34" height="22" viewBox="0 0 34 22"><path d="M2 12 L12 19 L32 3" fill="none" stroke="#f26522" stroke-width="4" stroke-linecap="round" stroke-linejoin="round"/></svg>Injectables</li>
    <li><svg width="34" height="22" viewBox="0 0 34 22"><path d="M2 12 L12 19 L32 3" fill="none" stroke="#f26522" stroke-width="4" stroke-linecap="round" stroke-linejoin="round"/></svg>Special Orders</li>
  </ul>

  <div class="delivery-pill">Delivery Service</div>
  <div class="hours">
    <div class="day">Monday – Saturday</div>
    <div class="day">Thursday</div>
    <div class="time">8am- 7pm</div>
    <div class="day">Sunday</div>
    <div class="time">10am-2pm</div>
  </div>

  <div class="product-display" role="img" aria-label="Photo of pharmacy products: blister packs of tablets, a syringe, a digital thermometer, a nasal spray and a pill bottle"></div>

  <svg class="contact-pin" width="38" height="48" viewBox="0 0 38 48">
    <path d="M19 1 C9 1 1 9 1 19 C1 31 19 47 19 47 C19 47 37 31 37 19 C37 9 29 1 19 1 Z" fill="#4a5da9"/>
    <circle cx="19" cy="18" r="7" fill="#fecb00"/>
  </svg>
  <div class="address">Unit B4, Palm Court Plaza,<br>Shore Road, Westhaven</div>

  <svg class="phone-icon" width="46" height="46" viewBox="0 0 46 46">
    <path d="M9 4 L16 4 L19 13 L14 17 C16 23 21 28 27 31 L31 26 L40 29 L40 36 C40 39 37 42 33 41 C18 38 7 27 4 12 C3 8 6 4 9 4 Z" fill="#4a5da9"/>
    <path d="M26 4 A16 16 0 0 1 42 20 M26 11 A9 9 0 0 1 35 20" fill="none" stroke="#4a5da9" stroke-width="3.5" stroke-linecap="round"/>
  </svg>
  <div class="phone-number">472-3086</div>

  <div class="social">Visit us on <div class="social-square"></div></div>
</div>
</body>
</html>
```